I work in creative/artistic projects across different mediums.
It needs to communicate creativity, style, sexy, uniqueness, individuality and sophistication.
It should not look corporate.
Colours I like are black silver gold deep purple, chocolate, orchid.
It doesn't have to make use of all these colours.
I do not like bright primary colors.
Updates

Project Deadline Extended
Reason: Still in the communication process and to allow the person enough time to finish the design. Though i should know in the next day or two. Thank you.

Target Market(s)

creatives and companies wanting to inject creativity into thier business.

Industry/Entity Type

Work

Contact Information for Business Card

Marcus Tellwick
0418592036
marcus@marcustellwick.com

quietgoldenhour.com.au

Requirements
Should not have
• Anything corporate OR OLD FASHIONED

```html
<!DOCTYPE html>
<html lang="en">
<head>
<meta charset="utf-8">
<title>Marcus Tellwick – Business Card</title>
<link rel="stylesheet" href="https://fonts.googleapis.com/css2?family=Arimo:ital,wght@0,400;1,400&display=swap">
<style>
  :root {
    --backdrop: #161616;
    --card-edge: #0d0a0f;
    --card-light: #5a2d6e;
    --card-mid: #3f1d4f;
    --card-deep: #26112f;
    --ink: #c9a54e;
    --ink-soft: #e0c47a;
  }
  * { box-sizing: border-box; margin: 0; padding: 0; }
  html, body {
    width: 1200px; height: 900px; overflow: hidden;
    background: var(--backdrop);
    font-family: "Arimo", Arial, sans-serif;
  }
  .stage {
    width: 1200px; height: 900px;
    display: flex; align-items: center; justify-content: center;
  }
  .card {
    position: relative;
    width: 1000px; height: 570px;
    border: 8px solid var(--card-edge);
    background: var(--card-mid);
    overflow: hidden;
  }
  .card__texture {
    position: absolute; inset: 0;
    background: radial-gradient(ellipse at 40% 45%, var(--card-light) 0%, var(--card-mid) 55%, var(--card-deep) 100%);
  }
  .card__top-bar {
    position: absolute; top: 14px; left: 520px; right: 0; height: 16px;
    background: var(--ink);
  }
  .card__name-bar {
    position: absolute; top: 118px; left: 360px; right: 110px; height: 28px;
    background: var(--ink);
  }
  .card__name {
    position: absolute; top: 112px; left: 30px;
    font-size: 34px; font-style: italic; font-weight: 400; color: var(--ink-soft);
  }
  .contact-list {
    position: absolute; top: 168px; left: 360px;
    list-style: none;
  }
  .contact-list__item {
    display: flex; align-items: center; height: 68px;
    font-size: 28px; color: var(--ink-soft);
  }
  .contact-list__icon {
    width: 64px; height: 48px; margin-right: 26px;
    display: flex; align-items: center; justify-content: center;
  }
  .contact-list__icon svg { fill: none; stroke: var(--ink); stroke-width: 3; }
  .contact-list__icon .icon-fill { fill: var(--ink); stroke: none; }
  .contact-list__icon .icon-cut { stroke: var(--card-mid); }
  .card__divider {
    position: absolute; top: 398px; left: 160px; right: 0; height: 8px;
    background: var(--ink);
  }
  .social {
    position: absolute;
    display: flex; align-items: center; gap: 10px;
    font-size: 22px; color: var(--ink-soft);
  }
  .social__mark {
    width: 22px; height: 22px; background: var(--ink); border-radius: 4px;
  }
  .social--chirpline { top: 440px; right: 26px; }
  .social--friendwall { bottom: 24px; left: 24px; }
</style>
</head>
<body>
<main class="stage">
  <article class="card">
    <div class="card__texture" role="img" aria-label="Soft deep purple background with a faint pattern of round dots"></div>
    <div class="card__top-bar"></div>
    <div class="card__name-bar"></div>
    <h1 class="card__name">Marcus Tellwick</h1>
    <ul class="contact-list">
      <li class="contact-list__item">
        <span class="contact-list__icon">
          <svg width="60" height="40" viewBox="0 0 60 40" aria-hidden="true">
            <rect class="icon-fill" x="2" y="2" width="56" height="36"/>
            <polyline class="icon-cut" points="4,5 30,24 56,5"/>
            <line class="icon-cut" x1="4" y1="36" x2="22" y2="19"/>
            <line class="icon-cut" x1="56" y1="36" x2="38" y2="19"/>
          </svg>
        </span>
        marcus@marcustellwick.com
      </li>
      <li class="contact-list__item">
        <span class="contact-list__icon">
          <svg width="28" height="46" viewBox="0 0 28 46" aria-hidden="true">
            <rect x="2" y="2" width="24" height="42" rx="4"/>
            <rect x="6" y="8" width="16" height="26"/>
          </svg>
        </span>
        0418592036
      </li>
      <li class="contact-list__item">
        <span class="contact-list__icon">
          <svg width="46" height="46" viewBox="0 0 46 46" aria-hidden="true">
            <circle cx="23" cy="23" r="20"/>
            <ellipse cx="23" cy="23" rx="9" ry="20"/>
            <line x1="3" y1="23" x2="43" y2="23"/>
            <line x1="23" y1="3" x2="23" y2="43"/>
            <path d="M7 12 H39 M7 34 H39"/>
          </svg>
        </span>
        quietgoldenhour.com.au
      </li>
    </ul>
    <div class="card__divider"></div>
    <div class="social social--chirpline"><span class="social__mark"></span>Chirpline</div>
    <div class="social social--friendwall"><span class="social__mark"></span>Friendwall</div>
  </article>
</main>
</body>
</html>
```